Bref créative
Quiet Harbor Dental Urgent Clinic- Business Cards and Stationary
Quiet Harbor Dental Urgent Clinic
Professional
Peter Delacroix, Jr., DMD
Founder/ CEO
2718 Pellam Rd
Ste 412
Houston, TX 77291
1-855-GRIN-WELLS
petedx4@mailvane.example
www.GRINWELLS.example
we can see you now!
RED, WHITE AND BLUE
I Have raised the $$$$ for postcard fabrication as well. let's get it!
attached is the graphic concept i'd like to achieve with the postcard.

```html
<!DOCTYPE html>
<html lang="en">
<head>
<meta charset="UTF-8">
<title>Quiet Harbor Dental Urgent Clinic – Business Card</title>
<link href="https://fonts.googleapis.com/css2?family=Cinzel:wght@400;600&display=swap" rel="stylesheet">
<style>
  :root {
    --page-bg: #e9e6e1;
    --card-white: #f7f7f6;
    --card-blue: #2f5ca8;
    --brand-blue: #2a5aa6;
    --brand-red: #d2452c;
    --ink-light: #eef2fa;
  }
  * { box-sizing: border-box; margin: 0; padding: 0; }
  html, body {
    width: 1200px; height: 901px; overflow: hidden;
    background: var(--page-bg);
    font-family: "Cinzel", serif;
  }
  .sheet {
    position: relative; width: 1200px; height: 901px;
    display: flex; align-items: center; justify-content: center; gap: 40px;
  }
  .card {
    position: relative; width: 540px; height: 309px; overflow: hidden;
    box-shadow: 0 6px 18px rgba(0,0,0,.18);
  }
  .card--front { background: var(--card-white); }
  .card--back { background: var(--card-blue); color: var(--ink-light); }

  .brand {
    position: absolute; left: 170px; top: 38px;
    display: flex; align-items: center; gap: 12px;
  }
  .brand__dot {
    flex: none; width: 36px; height: 36px; border-radius: 50%; background: var(--brand-blue);
  }
  .brand__name {
    color: var(--brand-blue); font-weight: 400; font-size: 15px;
    letter-spacing: .8px; line-height: 1.3; width: 230px;
  }

  .person { position: absolute; left: 42px; top: 196px; }
  .person__name { color: var(--brand-red); font-size: 21px; letter-spacing: .6px; }
  .person__suffix { font-size: 12px; }
  .person__role { color: var(--brand-blue); font-size: 13px; letter-spacing: 1px; margin-top: 4px; }

  .contact-web {
    position: absolute; right: 30px; top: 26px;
    font-size: 10px; letter-spacing: 1.4px;
  }
  .contact-address {
    position: absolute; right: 30px; top: 118px; text-align: right;
    font-style: normal; font-size: 10.5px; letter-spacing: 1.3px; line-height: 1.75;
  }
</style>
</head>
<body>
<main class="sheet">

  <section class="card card--front" aria-label="Business card front">
    <div class="brand">
      <span class="brand__dot"></span>
      <p class="brand__name">Quiet Harbor Dental Urgent Clinic</p>
    </div>
    <div class="person">
      <p class="person__name">Peter Delacroix, <span class="person__suffix">Jr., DMD</span></p>
      <p class="person__role">Founder/ CEO</p>
    </div>
  </section>

  <section class="card card--back" aria-label="Business card back">
    <p class="contact-web">www.GRINWELLS.example</p>
    <address class="contact-address">
      2718 Pellam Rd<br>
      Ste 412<br>
      Houston, TX 77291<br>
      Toll Free: 1-855-GRIN-WELLS<br>
      petedx4@mailvane.example
    </address>
  </section>

</main>
</body>
</html>
```